Business Card & Letter Head Design

Business Card:

We are looking for a business card design that consists of back and front.
The card size must be 85mm 55mm

The Full Brief is attached as a PDF. Please Download and Read

Industry/Entity Type

Business

```html
<!DOCTYPE html>
<html lang="en">
<head>
<meta charset="utf-8">
<title>Halden Security Letterhead</title>
<link rel="stylesheet" href="https://fonts.googleapis.com/css2?family=Carlito:wght@400;700&display=swap">
<style>
  :root {
    --backdrop: #c4c4c4;
    --paper: #ffffff;
    --band-blue: #3467b0;
    --band-text: #ffffff;
    --title-text: #e3ecf8;
    --footer-dark: #2e2927;
    --footer-gold: #f2c12e;
    --footer-text: #ffffff;
    --mark-dark: #1f1c1a;
  }
  * { margin: 0; padding: 0; box-sizing: border-box; }
  html, body {
    width: 1200px;
    height: 1071px;
    overflow: hidden;
    background: var(--backdrop);
    font-family: "Carlito", sans-serif;
  }
  .letterhead {
    position: absolute;
    left: 248px;
    top: 38px;
    width: 704px;
    height: 994px;
    background: var(--paper);
    box-shadow: 0 3px 10px rgba(0, 0, 0, 0.35);
  }
  .brand {
    position: absolute;
    left: 40px;
    top: 58px;
    width: 112px;
    display: flex;
    align-items: center;
    gap: 7px;
  }
  .brand-dot {
    flex: none;
    width: 16px;
    height: 16px;
    border-radius: 50%;
    background: var(--mark-dark);
  }
  .brand-name {
    font-weight: 700;
    font-size: 17px;
    line-height: 18px;
    color: var(--mark-dark);
  }
  .services-band {
    position: absolute;
    left: 162px;
    top: 31px;
    width: 542px;
    height: 90px;
    background: var(--band-blue);
  }
  .accreditation {
    position: absolute;
    left: 8px;
    top: 4px;
    width: 58px;
    height: 74px;
    background: var(--paper);
  }
  .services {
    position: absolute;
    left: 67px;
    right: 0;
    top: 19px;
    text-align: center;
    color: var(--band-text);
    font-weight: 700;
  }
  .services-title {
    font-size: 13.5px;
    color: var(--title-text);
    letter-spacing: 0.2px;
    margin-bottom: 9px;
  }
  .services-list {
    font-size: 11.8px;
    line-height: 12px;
  }
  .footer {
    position: absolute;
    left: 0;
    bottom: 0;
    width: 100%;
    height: 59px;
    background: var(--footer-dark);
    text-align: center;
    padding-top: 11px;
  }
  .footer-name {
    font-weight: 700;
    font-size: 14.5px;
    color: var(--footer-gold);
    line-height: 16px;
  }
  .footer-contact {
    font-size: 12.5px;
    color: var(--footer-text);
    line-height: 15px;
  }
</style>
</head>
<body>
  <main class="letterhead">
    <div class="brand">
      <span class="brand-dot"></span>
      <span class="brand-name">Halden<br>Security</span>
    </div>

    <header class="services-band">
      <div class="accreditation" role="img" aria-label="Accreditation badge"></div>
      <div class="services">
        <p class="services-title">SPECIALIST SECURITY SERVICES</p>
        <p class="services-list">▪ Static &amp; Mobile Security Guards ▪ Key Holding &amp; Alarm Response<br>▪ CCTV Remote Monitoring ▪ Door Supervisors</p>
      </div>
    </header>

    <footer class="footer">
      <p class="footer-name">Halden Security Group</p>
      <p class="footer-contact">Ferncroft Road ▪ Ashby Vale ▪ Northfield ▪ NF47QT ▪ Phone: 01632 960913 ▪ Fax: 01632 960914</p>
    </footer>
  </main>
</body>
</html>
```